Customer Facing Document Design

Looking for professional design in Word for 5 Templates:

- Purchase Contract
- Sales Contract
- Packing List
- Settlement Report
- Invoice

I have attached our current designs and also some example designs that we want to look similar to. We want our company logo included on all documents. On the Purchase Order, Sales Order, Settlement Report, Invoice we also want our ISO accreditation picture and BQRF logo included.

```html
<!DOCTYPE html>
<html lang="en">
<head>
<meta charset="utf-8">
<title>Settlement Report</title>
<link href="https://fonts.googleapis.com/css2?family=Montserrat:wght@400;500;700;800&display=swap" rel="stylesheet">
<style>
  :root {
    --backdrop: #b1b1b1;
    --paper: #ffffff;
    --ink: #111111;
    --brand-grey: #6a6a6a;
    --brand-light: #9a9a9a;
    --rule: #111111;
  }
  * { margin: 0; padding: 0; box-sizing: border-box; }
  html, body { width: 915px; height: 1200px; overflow: hidden; }
  body { background: var(--backdrop); font-family: "Montserrat", sans-serif; color: var(--ink); position: relative; }
  .sheet { position: absolute; left: 103px; top: 327px; width: 709px; height: 548px; background: var(--paper); }
  .abs { position: absolute; }

  .assoc-mark { left: 44px; top: 55px; display: flex; align-items: center; gap: 5px; }
  .assoc-mark .name { font-size: 32px; font-weight: 800; color: var(--brand-grey); letter-spacing: 1px; line-height: 1; }
  .assoc-mark .dot { width: 32px; height: 32px; border-radius: 50%; background: var(--brand-grey); }

  .cert-badge { left: 309px; top: 25px; width: 110px; height: 100px; background: #1a1a1a; }

  .company-mark { left: 502px; top: 40px; display: flex; align-items: center; gap: 6px; }
  .company-mark .dot { width: 70px; height: 70px; border-radius: 50%; background: var(--brand-light); }
  .company-mark .name { font-size: 22px; font-weight: 800; color: var(--brand-grey); line-height: 1; }

  .contact { left: 44px; top: 145px; font-size: 10.2px; line-height: 12.5px; letter-spacing: 0.3px; color: #222; font-style: normal; }

  .doc-title { left: 43px; top: 237px; font-size: 11.6px; font-weight: 700; letter-spacing: 0.2px; }

  .meta { left: 84px; top: 268px; font-size: 6.8px; line-height: 12.5px; }
  .meta span { display: inline-block; width: 40px; }
  .dates { font-size: 7.8px; }
  .dates.issue { left: 517px; top: 277px; }
  .dates.received { left: 476px; top: 294px; }

  .ledger { left: 44px; top: 316px; border-collapse: collapse; table-layout: fixed; font-size: 6.7px; }
  .ledger td, .ledger th { border: 1px solid var(--rule); height: 10.6px; padding: 0 3px; font-weight: 400; text-align: left; white-space: nowrap; vertical-align: middle; }
  .ledger th.item, .ledger td.item { text-align: center; font-weight: 700; font-size: 5.8px; }
  .ledger .price { text-align: center; }
  .ledger .amount { text-align: right; }
  .ledger .bare { border: none; }
  .ledger .total-label, .ledger .grand { font-weight: 700; }
</style>
</head>
<body>
  <main class="sheet">
    <div class="abs assoc-mark"><span class="name">BQRF</span><span class="dot"></span></div>
    <div class="abs cert-badge" role="img" aria-label="Accreditation badge"></div>
    <div class="abs company-mark"><span class="dot"></span><span class="name">ORVELLIC</span></div>

    <address class="abs contact">
      ORVELLIC ALLOYS &amp; METALS,<br>
      LLC OPS@ORVELLIC-AM.COM<br>
      +44 7700 900412<br>
      WWW.ORVELLIC-AM.COM<br>
      1480 LINDELL COURT, FAIRVIEW. CA 90299
    </address>

    <h1 class="abs doc-title">SETTLEMENT REPOR</h1>

    <div class="abs meta">
      <div><span>SUPPLIER:</span>NORTHGATE RECYCLING</div>
      <div><span>Lot No:</span>&nbsp;877</div>
      <div><span>PO No.:</span></div>
    </div>
    <div class="abs dates issue">DATE: September 19, 2025</div>
    <div class="abs dates received">RECEIVING DATE: August 11, 2025</div>

    <table class="abs ledger">
      <colgroup>
        <col style="width:38px"><col style="width:133.5px"><col style="width:142.5px"><col style="width:58px">
        <col style="width:63px"><col style="width:74px"><col style="width:5.5px"><col style="width:107px">
      </colgroup>
      <tr><th class="item">ITEM NO.</th><th>Advised As:</th><th>Graded As:</th><th>Advised (Lbs)</th><th>Received (Lbs)</th><th class="price">$ / LB</th><th></th><th></th></tr>
      <tr><td class="item">1</td><td>Alloy 718 Turnings</td><td>Alloy 718 Turnings - 1% Alum 1% Fe</td><td></td><td>284</td><td class="price">$5.2000</td><td></td><td class="amount">$1,476.80</td></tr>
      <tr><td class="item">2</td><td></td><td>Alloy 718 Turnings - 1% Alum 1% Fe</td><td></td><td>1382</td><td class="price">$5.2000</td><td></td><td class="amount">$7,186.40</td></tr>
      <tr><td class="item">3</td><td></td><td>Alloy 718 Turnings - 1% Alum 1% Fe</td><td></td><td>1390</td><td class="price">$5.2000</td><td></td><td class="amount">$7,228.00</td></tr>
      <tr><td class="item">4</td><td></td><td>Steel Turnings</td><td></td><td>556</td><td class="price">$5.2000</td><td></td><td class="amount">$0.00</td></tr>
      <tr><td class="item">5</td><td></td><td>Alloy 718 Turnings - 1% Alum 1% Fe</td><td></td><td>1340</td><td class="price">$5.2000</td><td></td><td class="amount">$6,968.00</td></tr>
      <tr><td class="item">6</td><td></td><td>Alloy 718 Turnings - 1% Alum 1% Fe</td><td></td><td>1528</td><td class="price">$5.2000</td><td></td><td class="amount">$7,945.60</td></tr>
      <tr><td></td><td></td><td></td><td></td><td></td><td></td><td></td><td></td></tr>
      <tr><td class="bare"></td><td class="bare"></td><td class="bare"></td><td>0</td><td>6,480&nbsp;&nbsp;6,480</td><td class="total-label">Total</td><td></td><td class="amount grand">$30,804.80</td></tr>
    </table>
  </main>
</body>
</html>
```